Biz Card for Harrowfield Property Partners - HWPP

Harrowfield Property Partners is a commercial real estate acquisitions firm. We buy commercial property and need to raise capital from investors for each deal we buy. The vibe needs to be: give us your money, we will multiply it.
Our website: www.hrwpp-example.com
Competitors are: https://velmarholdings-example.com/, https://tribanquepartners-example.com/, http://www.ostrellecapital-example.com/
Target Market(s)
High Net Worth Individuals, Bankers, Insurance Companies, Commercial Real Estate Brokers.
Industry/Entity Type
Investment Banking
Contact Information for Business Card
Name, Title, Addess, Cell#, Office#, email, website
Requirements
Must have
- use one of our logos. See website for look and feel: www.hrwpp-example.com
Nice to have
- see website: www.hrwpp-example.com

```html
<!DOCTYPE html>
<html lang="en">
<head>
<meta charset="UTF-8">
<title>Harrowfield Property Partners – Business Card</title>
<link href="https://fonts.googleapis.com/css2?family=Lato:wght@400;700&display=swap" rel="stylesheet">
<style>
  :root {
    --navy: #0c2a45;
    --paper: #ffffff;
    --ink-soft: #6b7480;
    --ink-mid: #5a6270;
    --rule: #9aa3ad;
    --backdrop: #e9ebee;
  }
  * { margin: 0; padding: 0; box-sizing: border-box; }
  html, body {
    width: 1200px; height: 1000px; overflow: hidden;
    background: var(--backdrop);
    font-family: "Lato", Arial, sans-serif;
  }
  .canvas { position: relative; width: 1200px; height: 1000px; }

  .card {
    position: absolute;
    width: 560px; height: 320px;
    border-radius: 22px;
    overflow: hidden;
  }

  /* Back of card */
  .card-back {
    left: 80px; top: 100px;
    background: var(--navy);
    display: flex; flex-direction: column; align-items: center; justify-content: center;
    color: var(--paper);
  }
  .brand {
    display: flex; flex-direction: column; align-items: center;
    font-weight: 400;
  }
  .brand-mark {
    width: 78px; height: 78px; border-radius: 50%;
    margin-bottom: 16px;
  }
  .card-back .brand-mark { background: var(--paper); }
  .brand-name {
    font-size: 40px; letter-spacing: 7px; line-height: 1; text-transform: uppercase;
  }
  .brand-sub {
    font-size: 15px; letter-spacing: 5px; margin-top: 8px; text-transform: uppercase;
  }

  /* Front of card */
  .card-front {
    left: 560px; top: 580px;
    background: var(--paper);
    color: var(--navy);
  }
  .card-front .brand {
    position: absolute; left: 24px; top: 56px; width: 270px;
  }
  .card-front .brand-mark { background: var(--navy); width: 70px; height: 70px; margin-bottom: 14px; }
  .card-front .brand-name { font-size: 26px; letter-spacing: 4px; }
  .card-front .brand-sub { font-size: 11px; letter-spacing: 3.5px; }

  .divider {
    position: absolute; left: 302px; top: 36px;
    width: 1px; height: 170px;
    background: linear-gradient(to bottom, var(--rule), rgba(154,163,173,0.2));
  }

  .contact {
    position: absolute; left: 326px; top: 36px;
  }
  .person-name { font-size: 22px; font-weight: 700; color: var(--navy); }
  .person-title { font-size: 14px; color: var(--ink-soft); margin-top: 4px; margin-bottom: 12px; }
  .contact-list { list-style: none; }
  .contact-list li {
    display: flex; align-items: center; gap: 9px;
    font-size: 13px; color: var(--ink-mid); margin-bottom: 6px;
  }
  .contact-icon { width: 16px; height: 16px; flex: none; }

  .address-band {
    position: absolute; left: 0; right: 0; top: 226px; height: 52px;
    background: var(--navy); color: var(--paper);
    display: flex; align-items: center; justify-content: center;
    font-size: 16px; letter-spacing: 0.4px;
  }
</style>
</head>
<body>
<main class="canvas">

  <section class="card card-back" aria-label="Business card back">
    <div class="brand">
      <span class="brand-mark"></span>
      <span class="brand-name">Harrowfield</span>
      <span class="brand-sub">Property Partners</span>
    </div>
  </section>

  <section class="card card-front" aria-label="Business card front">
    <div class="brand">
      <span class="brand-mark"></span>
      <span class="brand-name">Harrowfield</span>
      <span class="brand-sub">Property Partners</span>
    </div>

    <div class="divider"></div>

    <div class="contact">
      <p class="person-name">Daniel Ashcombe</p>
      <p class="person-title">Founder/CEO</p>
      <ul class="contact-list">
        <li>
          <svg class="contact-icon" viewBox="0 0 16 16" aria-hidden="true">
            <circle cx="8" cy="8" r="8" fill="#0c2a45"/>
            <path d="M5.2 4.2l1.4-.2.8 1.9-.9.7c.4.9 1.1 1.6 2 2l.7-.9 1.9.8-.2 1.4c-3 .3-6-2.7-5.7-5.7z" fill="#fff"/>
          </svg>
          (555) 014-2280
        </li>
        <li>
          <svg class="contact-icon" viewBox="0 0 16 16" aria-hidden="true">
            <circle cx="8" cy="8" r="8" fill="#0c2a45"/>
            <path d="M3.8 6.4c2.6-2 5.8-2 8.4 0l-.5 1.3-1.6-.3-.2-1.1c-1.2-.4-2.6-.4-3.8 0l-.2 1.1-1.6.3z" fill="#fff"/>
            <rect x="5" y="8.6" width="6" height="3" rx="0.8" fill="#fff"/>
          </svg>
          (555) 014-2281
        </li>
        <li>
          <svg class="contact-icon" viewBox="0 0 16 16" aria-hidden="true">
            <circle cx="8" cy="8" r="8" fill="#0c2a45"/>
            <rect x="4" y="5.2" width="8" height="5.6" rx="0.6" fill="#fff"/>
            <path d="M4.3 5.6L8 8.4l3.7-2.8" fill="none" stroke="#0c2a45" stroke-width="0.9"/>
          </svg>
          dashcombe@hrwpp-example.com
        </li>
        <li>
          <svg class="contact-icon" viewBox="0 0 16 16" aria-hidden="true">
            <circle cx="8" cy="8" r="8" fill="#0c2a45"/>
            <g fill="none" stroke="#fff" stroke-width="0.9">
              <circle cx="8" cy="8" r="4"/>
              <ellipse cx="8" cy="8" rx="1.8" ry="4"/>
              <path d="M4 8h8"/>
            </g>
          </svg>
          www.hrwpp-example.com
        </li>
      </ul>
    </div>

    <div class="address-band">418 Larkmoor Ave, Suite 900 Westbury Bay, FL 30010</div>
  </section>

</main>
</body>
</html>
```